依頼詳細
PCとスマホデザインの両方納品をいただきますが、
まずはデザインイメージが確認しやすいPCページのみの提案をお願いします。
スマホページは当選者に納品時にお願いしたいと思います。
スマホサイズは横幅750pxのサイズで作成してください。

レスポンシブウェブデザインを意識したデザインでお願いします。

デザインに関しては、添付してあるデザインレイアウト設計シートを基にお願いします。
参考サイトのURLはデザインレイアウト設計シートに記載してあります。

画像データについては、既存サイトや参考サイト、フリー素材から流用してイメージ画像に当て込んでください。
足りない場合は、一旦他のサイトの写真をサンプルとして入れてください。(サンプルなどの表記をお願いします)
ページ数
1ページ
希望イメージ
シンプル 複雑
単色 カラフル
暗い 明るい
日常 高級
遊び心 厳粛
未来的 伝統的
女性的 男性的
希望する色
青系、水色系、明るい色味
納品ファイル
• 高解像度JPG (.jpg)
• イラストレーター形式 (.ai)
• フォトショップ形式 (.psd)
• PNG形式 (.png)
補足説明
上記のいずれか1つ。アウトラインありとなしの2つ。

クライアントのイメージ通りでした。

たくさんのご提案ありがとうございました。
次回もぜひ、よろしくお願い致します。

```html
<!DOCTYPE html>
<html lang="ja">
<head>
<meta charset="utf-8">
<title>ミライ・プロダクツ</title>
<link href="https://fonts.googleapis.com/css2?family=Noto+Sans+JP:wght@400;500;700;900&family=Oswald:wght@500;600;700&display=swap" rel="stylesheet">
<style>
:root{
  --cyan:#17b3e6;
  --cyan-dark:#0e9ccc;
  --pale:#e4f5fc;
  --pale2:#d3eef9;
  --navy:#1f3552;
  --text:#333c47;
  --yellow:#ffe83a;
  --white:#ffffff;
  --line:#d6dde3;
}
*{box-sizing:border-box;margin:0;padding:0}
html,body{width:1200px;height:4532px;overflow:hidden}
body{font-family:"Noto Sans JP",sans-serif;color:var(--text);background:var(--white);position:relative}
.en{font-family:"Oswald",sans-serif}
.abs{position:absolute}

/* header */
.site-header{position:absolute;top:0;left:0;width:1200px;height:80px;z-index:5}
.brand{position:absolute;left:30px;top:14px;height:50px;padding:0 26px;background:var(--cyan);border-radius:25px;color:var(--white);font:700 30px/50px "Oswald",sans-serif;letter-spacing:3px}
.gnav{position:absolute;left:350px;top:0;display:flex;height:80px}
.gnav a{display:flex;flex-direction:column;align-items:center;justify-content:center;width:128px;color:var(--navy);text-decoration:none;border-left:1px solid #b9dbe8;font-weight:700;font-size:16px}
.gnav a:last-child{border-right:1px solid #b9dbe8}
.gnav small{font:500 10px "Oswald",sans-serif;color:var(--cyan);letter-spacing:1px;margin-top:4px}
.store{position:absolute;right:0;top:0;width:120px;height:150px;background:var(--cyan);color:var(--white);text-align:center;padding-top:18px;font:600 18px/1.1 "Oswald",sans-serif}
.store svg{display:block;margin:0 auto 10px}

/* hero */
.hero{position:absolute;top:0;left:0;width:1200px;height:740px;background:var(--pale)}
.ph{position:absolute;border-radius:14px}
.hero-copy{position:absolute;top:320px;left:0;width:1200px;text-align:center;font-weight:900;font-size:38px;line-height:60px;color:var(--navy)}
.hero-copy em{font-style:normal;background:var(--yellow);padding:0 6px;color:var(--navy)}
.btn{display:inline-block;width:240px;height:56px;border-radius:28px;background:var(--cyan);color:var(--white);font-weight:700;font-size:17px;line-height:56px;text-align:center;box-shadow:0 4px 0 var(--cyan-dark)}
.scroll{position:absolute;left:570px;top:634px;width:60px;text-align:center;font:500 11px "Oswald",sans-serif;color:var(--navy)}
.scroll span{display:block;width:44px;height:44px;margin:6px auto 0;border:2px solid var(--navy);border-radius:50%}

/* about concept */
.concept{position:absolute;top:740px;left:0;width:1200px;height:600px;background:var(--cyan);color:var(--white);text-align:center}
.concept .sub{margin-top:44px;font:500 16px "Oswald",sans-serif;letter-spacing:2px}
.concept h2{font-size:42px;font-weight:900;margin-top:4px}
.concept p{margin-top:30px;font-size:18px;line-height:34px;font-weight:500}
.concept p b{color:var(--yellow)}
.flow{position:absolute;top:370px;left:140px;display:flex;align-items:flex-start}
.flow .step{width:150px;text-align:center;font-weight:700;font-size:16px}
.flow .circle{width:130px;height:130px;margin:0 auto 12px;border-radius:50%;border:3px solid var(--white);display:flex;align-items:center;justify-content:center}
.flow .final .circle{background:var(--yellow);border-color:var(--yellow)}
.flow .final{color:var(--yellow)}
.flow .op{width:110px;text-align:center;font-size:44px;line-height:134px;font-weight:300}

/* section title */
.sec-title{text-align:center}
.sec-title h2{font:700 54px/1 "Oswald",sans-serif;color:var(--cyan);letter-spacing:4px}
.sec-title p{font-weight:700;font-size:15px;color:var(--navy);margin-top:10px}

/* product */
.product{position:absolute;top:1340px;left:0;width:1200px;height:650px;background:var(--white)}
.product .sec-title{margin-top:130px}
.cards{position:absolute;top:270px;left:140px;display:flex;gap:30px}
.card{width:210px;text-align:center;font-size:14px;font-weight:500;line-height:22px;color:var(--navy)}
.card .thumb{height:200px;border-radius:4px;margin-bottom:12px}
.new{position:absolute;top:236px;left:188px;font:italic 700 16px "Oswald",sans-serif;color:#e6a800}
.arrow{position:absolute;top:400px;width:30px;height:60px}
.dots{position:absolute;top:590px;left:0;width:1200px;display:flex;justify-content:center;gap:10px}
.dots i{width:10px;height:10px;border-radius:50%;background:#cfe9f4}
.dots i:first-child{background:var(--cyan)}

/* category */
.category{position:absolute;top:1990px;left:0;width:1200px;height:650px;background:var(--pale)}
.big-word{position:absolute;left:-6px;top:-4px;writing-mode:vertical-rl;font:700 150px/1 "Oswald",sans-serif;color:rgba(255,255,255,.9);letter-spacing:12px}
.cat-grid{position:absolute;top:60px;left:140px;width:920px;display:grid;grid-template-columns:repeat(4,215px);gap:20px 20px}
.cat-grid a{display:block;height:56px;background:var(--white);border:2px solid var(--cyan);line-height:52px;padding-left:22px;font-weight:700;font-size:15px;color:var(--navy);text-decoration:none;box-shadow:4px 4px 0 var(--pale2)}
.category .btn{position:absolute;top:525px;left:480px}

/* information */
.info{position:absolute;top:2640px;left:0;width:1200px;height:440px;background:var(--white)}
.info .sec-title{margin-top:60px}
.news{position:absolute;top:170px;left:140px;width:920px;list-style:none}
.news li{height:60px;border-bottom:1px solid var(--line);display:flex;align-items:center;font-size:14px;color:var(--text)}
.news li:first-child{border-top:1px solid var(--line)}
.news time{width:150px;padding-left:20px;color:#8a96a3;font-size:13px}
.info .btn{position:absolute;top:355px;left:480px}

/* about us */
.aboutus{position:absolute;top:3080px;left:0;width:1200px;height:620px;background:var(--pale)}
.aboutus .sec-title{margin-top:70px}
.about-cards{position:absolute;top:200px;left:140px;display:flex;gap:48px}
.about-card{width:275px;height:300px;background:var(--white);border:3px solid var(--cyan);text-align:center;box-shadow:8px 8px 0 var(--pale2)}
.about-card.shop{background:#fffbd6}
.about-card .ico{width:86px;height:86px;margin:26px auto 14px;border-radius:50%;background:var(--cyan);display:flex;align-items:center;justify-content:center}
.about-card h3{font-size:20px;font-weight:900;color:var(--cyan-dark);margin-bottom:14px}
.about-card p{font-size:14px;line-height:23px;font-weight:500;color:var(--navy)}

/* contact */
.contact{position:absolute;top:3700px;left:0;width:1200px;height:380px;background:var(--white);overflow:hidden}
.contact .diag{position:absolute;top:0;left:0}
.contact .col{position:absolute;top:34px;width:600px;text-align:center}
.contact .col p.lead{font-size:15px;line-height:26px;margin:24px 0 28px;color:var(--navy)}
.to-top{position:absolute;right:50px;top:280px;width:64px;height:64px;border-radius:50%;background:var(--cyan);display:flex;align-items:center;justify-content:center}

/* footer */
.site-footer{position:absolute;top:4080px;left:0;width:1200px;height:452px;background:var(--white);border-top:1px solid var(--line)}
.site-footer .brand{left:140px;top:40px}
.flinks{position:absolute;top:130px;display:flex;flex-direction:column;gap:10px;list-style:none;font-size:14px;color:var(--navy)}
.flinks li::before{content:"›";color:var(--cyan);margin-right:8px;font-weight:700}
.search-h{position:absolute;left:700px;top:100px;font:600 16px "Oswald",sans-serif;color:var(--cyan);letter-spacing:1px}
.search-box{position:absolute;left:700px;top:130px;width:360px;height:36px;border:1px solid var(--line);font-size:13px;line-height:34px;padding-left:36px;color:#9aa4ad}
.search-box svg{position:absolute;left:10px;top:9px}
.company{position:absolute;left:700px;top:210px;font-size:14px;font-weight:700;color:var(--navy);line-height:24px}
.company small{display:block;font-weight:400;font-size:12px;line-height:20px;color:var(--text)}
.tel{position:absolute;left:700px;top:300px;font:700 28px/34px "Oswald",sans-serif;color:var(--cyan-dark)}
.copyright{position:absolute;left:0;bottom:0;width:1200px;height:34px;background:var(--cyan);color:var(--white);text-align:center;font-size:11px;line-height:34px}
</style>
</head>
<body>

<header class="site-header">
  <div class="brand">MIRAI</div>
  <nav class="gnav">
    <a href="#">商品一覧<small>PRODUCT</small></a>
    <a href="#">卸業者さまへ<small>TO USERS</small></a>
    <a href="#">会社案内<small>ABOUT US</small></a>
    <a href="#">WEBカタログ<small>CATALOG</small></a>
    <a href="#">お問い合わせ<small>CONTACT</small></a>
  </nav>
  <div class="store">
    <svg width="52" height="46" viewBox="0 0 52 46" fill="none" stroke="#fff" stroke-width="4" stroke-linejoin="round" stroke-linecap="round"><path d="M2 4h8l6 26h28l5-18H13"/><circle cx="20" cy="40" r="3.5"/><circle cx="40" cy="40" r="3.5"/></svg>
    ONLINE<br>Store
  </div>
</header>

<section class="hero">
  <div class="ph" role="img" aria-label="商品写真：スポンジ" style="left:120px;top:90px;width:130px;height:80px;background:linear-gradient(#f3f3f3,#d94a4a)"></div>
  <div class="ph" role="img" aria-label="商品写真：黒い収納ケース" style="left:320px;top:96px;width:120px;height:70px;background:linear-gradient(#4a4d52,#23262a)"></div>
  <div class="ph" role="img" aria-label="商品写真：折りたたみ容器" style="left:530px;top:110px;width:120px;height:110px;background:linear-gradient(#f0f0ee,#bfc3c6)"></div>
  <div class="ph" role="img" aria-label="商品写真：オレンジのブラシ" style="left:690px;top:110px;width:80px;height:90px;background:linear-gradient(#ffb06a,#f07a1c);border-radius:40px"></div>
  <div class="ph" role="img" aria-label="商品写真：ピンクのパーツ" style="left:850px;top:120px;width:170px;height:130px;background:linear-gradient(#ffd1dd,#ef7e9d)"></div>
  <div class="ph" role="img" aria-label="商品写真：包丁" style="left:40px;top:380px;width:100px;height:40px;background:linear-gradient(90deg,#7a1d1d,#c9cdd1)"></div>
  <div class="ph" role="img" aria-label="商品写真：片手鍋" style="left:100px;top:440px;width:140px;height:100px;background:linear-gradient(#e7e9ea,#9aa0a6)"></div>
  <div class="ph" role="img" aria-label="商品写真：カラフルな歯ブラシ" style="left:820px;top:330px;width:180px;height:120px;background:linear-gradient(90deg,#ff6b8b,#ffd84a,#6fd0ff,#7be38b)"></div>
  <div class="ph" role="img" aria-label="商品写真：黄色いスコップ" style="left:1060px;top:230px;width:90px;height:240px;background:linear-gradient(#ffd21f,#f0b400)"></div>
  <div class="ph" role="img" aria-label="商品写真：ヘルメット" style="left:20px;top:560px;width:180px;height:110px;background:linear-gradient(#e6d3b8,#8c7458)"></div>
  <div class="ph" role="img" aria-label="商品写真：ルーペ" style="left:250px;top:580px;width:80px;height:80px;background:linear-gradient(#fff,#e24b3c);border-radius:40px"></div>
  <div class="ph" role="img" aria-label="商品写真：懐中電灯" style="left:400px;top:560px;width:140px;height:100px;background:linear-gradient(#ffe07a,#3c3f45)"></div>
  <div class="ph" role="img" aria-label="商品写真：作業用スツール" style="left:680px;top:560px;width:180px;height:110px;background:linear-gradient(#1fa9d8,#2b3f52)"></div>
  <div class="ph" role="img" aria-label="商品写真：洗剤パッケージ" style="left:900px;top:530px;width:130px;height:140px;background:linear-gradient(#f4fbe4,#9ed36a)"></div>
  <div class="ph" role="img" aria-label="商品写真：ランタン" style="left:1090px;top:540px;width:80px;height:140px;background:linear-gradient(#3c3f45,#8a8f96)"></div>

  <h1 class="hero-copy">ミライ・プロダクツの商品が<br>日々の生活に<em>新提案!</em></h1>
  <div style="position:absolute;top:480px;left:480px"><span class="btn">商品一覧</span></div>
  <div class="scroll">SCROLL<span><svg width="40" height="40" viewBox="0 0 40 40"><path d="M13 16l7 7 7-7" fill="none" stroke="#1f3552" stroke-width="2.5"/></svg></span></div>
</section>

<section class="concept">
  <p class="sub">What is MIRAI PRODUCTS?</p>
  <h2>ミライ・プロダクツとは、</h2>
  <p>「生活用品」「アイデア商品」の<b>オリジナル企画・開発、製造、卸まで</b>を、一貫して行っています。<br>
  常に、生活の変化に目を向け、お客様の視点に立ち、ただ単に安い商品ではなく、<br>
  <b>「毎日の暮らしを豊かにしてくれるもの」「便利にしてくれるもの」</b>を考えて、<br>
  オンリーワン商品の開発に取り組んでいます。</p>
  <div class="flow">
    <div class="step"><div class="circle"><svg width="60" height="60" viewBox="0 0 60 60" fill="none" stroke="#fff" stroke-width="4" stroke-linecap="round"><path d="M30 8a16 16 0 0 0-9 29v7h18v-7a16 16 0 0 0-9-29z"/><path d="M23 52h14"/></svg></div>企画・開発</div>
    <div class="op">×</div>
    <div class="step"><div class="circle"><svg width="60" height="60" viewBox="0 0 60 60" fill="none" stroke="#fff" stroke-width="4" stroke-linecap="round" stroke-linejoin="round"><path d="M38 10a10 10 0 0 0-12 13L10 39l6 6 16-16a10 10 0 0 0 13-12l-6 6-6-2-2-6z"/></svg></div>製 造</div>
    <div class="op">×</div>
    <div class="step"><div class="circle"><svg width="64" height="60" viewBox="0 0 64 60" fill="#fff"><rect x="4" y="14" width="34" height="26" rx="2"/><path d="M40 22h12l8 10v8H40z"/><circle cx="16" cy="44" r="6"/><circle cx="50" cy="44" r="6"/></svg></div>卸</div>
    <div class="op">=</div>
    <div class="step final"><div class="circle"><svg width="64" height="64" viewBox="0 0 64 64" fill="#1f3552"><path d="M26 6l5 17 17 5-17 5-5 17-5-17-17-5 17-5z"/><path d="M48 34l3 9 9 3-9 3-3 9-3-9-9-3 9-3z"/></svg></div>質の高い商品</div>
  </div>
</section>

<section class="product">
  <div class="sec-title"><h2>PRODUCT</h2><p>商品紹介</p></div>
  <span class="new">NEW!</span>
  <svg class="arrow" style="left:60px" viewBox="0 0 30 60"><path d="M22 14L8 30l14 16" fill="none" stroke="#17b3e6" stroke-width="5"/></svg>
  <svg class="arrow" style="right:60px" viewBox="0 0 30 60"><path d="M8 14l14 16-14 16" fill="none" stroke="#17b3e6" stroke-width="5"/></svg>
  <div class="cards">
    <div class="card"><div class="thumb" role="img" aria-label="商品写真：折りたたみ式ポータブルファン" style="background:linear-gradient(#bfe3f5,#5f9fc2)"></div>折りたたみ式<br>ポータブルファン</div>
    <div class="card"><div class="thumb" role="img" aria-label="商品写真：電動カッター" style="background:linear-gradient(#3a8fd0,#e9eef2)"></div>乗りも<br>電動カッター</div>
    <div class="card"><div class="thumb" role="img" aria-label="商品写真：シリコンハンディータワシ" style="background:linear-gradient(#e3f3fb,#7cc3e6)"></div>シリコンハンディータワシ<br>CLEANA(クリーナ)</div>
    <div class="card"><div class="thumb" role="img" aria-label="商品写真：収納ケース" style="background:linear-gradient(#f7f7f7,#bfc5ca)"></div>ピタッと収まる<br>収納ケース</div>
    <div class="card"><div class="thumb" role="img" aria-label="商品写真：ピンクの便利グッズ" style="background:linear-gradient(#ffe0e8,#ee7f9e)"></div>パパッと片付く<br>いつでも3個</div>
  </div>
  <div class="dots"><i></i><i></i><i></i></div>
</section>

<section class="category">
  <div class="big-word">PRODUCT</div>
  <div class="cat-grid">
    <a href="#">日本製品</a><a href="#">アイデア商品</a><a href="#">収納用品</a><a href="#">キッチン用品</a>
    <a href="#">LED商品</a><a href="#">環境用品</a><a href="#">保護商品/防犯用品</a><a href="#">ガーデニング用品</a>
    <a href="#">アウトドア用品</a><a href="#">工具用品</a><a href="#">防災用品</a><a href="#">生活用品</a>
    <a href="#" style="grid-column:2">健康器具/快適グッズ</a><a href="#">各種用品</a>
  </div>
  <span class="btn">商品一覧</span>
</section>

<section class="info">
  <div class="sec-title"><h2>INFORMATION</h2><p>お知らせ</p></div>
  <ul class="news">
    <li><time>2020.00.00</time>テキストテキストテキストテキストテキストテキストテキストテキスト</li>
    <li><time>2020.00.00</time>テキストテキストテキストテキストテキストテキストテキストテキスト</li>
    <li><time>2020.00.00</time>テキストテキストテキストテキストテキストテキストテキストテキスト</li>
  </ul>
  <span class="btn">お知らせ一覧</span>
</section>

<section class="aboutus">
  <div class="sec-title"><h2>ABOUT US</h2><p>会社案内</p></div>
  <div class="about-cards">
    <div class="about-card"><div class="ico"><svg width="44" height="44" viewBox="0 0 44 44" fill="#fff"><rect x="8" y="4" width="20" height="36"/><rect x="28" y="16" width="10" height="24"/><g fill="#17b3e6"><rect x="12" y="9" width="4" height="4"/><rect x="20" y="9" width="4" height="4"/><rect x="12" y="17" width="4" height="4"/><rect x="20" y="17" width="4" height="4"/><rect x="12" y="25" width="4" height="4"/><rect x="20" y="25" width="4" height="4"/></g></svg></div><h3>企業情報</h3><p>テキストテキストテキスト<br>テキストテキストテキスト<br>テキストテキスト</p></div>
    <div class="about-card"><div class="ico"><svg width="44" height="44" viewBox="0 0 44 44" fill="none" stroke="#fff" stroke-width="3.5"><path d="M22 10c-5-4-12-4-16-2v28c4-2 11-2 16 2 5-4 12-4 16-2V8c-4-2-11-2-16 2zM22 10v28"/></svg></div><h3>WEBカタログ</h3><p>テキストテキストテキスト<br>テキストテキストテキスト<br>テキストテキスト</p></div>
    <div class="about-card shop"><div class="ico"><svg width="46" height="42" viewBox="0 0 52 46" fill="none" stroke="#fff" stroke-width="4" stroke-linejoin="round" stroke-linecap="round"><path d="M2 4h8l6 26h28l5-18H13"/><circle cx="20" cy="40" r="3.5"/><circle cx="40" cy="40" r="3.5"/></svg></div><h3>ネットショップ</h3><p>テキストテキストテキスト<br>テキストテキストテキスト<br>テキストテキスト</p></div>
  </div>
</section>

<section class="contact">
  <svg class="diag" width="1200" height="380" viewBox="0 0 1200 380"><polygon points="640,0 1200,0 1200,380 560,380" fill="#e4f5fc"/></svg>
  <div class="col" style="left:0"><div class="sec-title"><h2>CONTACT</h2><p>お問い合わせ</p></div><p class="lead">ミライ・プロダクツへの<br>お問い合わせはこちらから</p><span class="btn">お問い合わせ</span></div>
  <div class="col" style="left:600px"><div class="sec-title"><h2>Q&amp;A</h2><p>よくあるご質問</p></div><p class="lead">お客様から寄せられた、よくあるご質問に<br>お答えしています。</p><span class="btn">よくあるご質問</span></div>
  <div class="to-top"><svg width="30" height="30" viewBox="0 0 30 30"><path d="M7 19l8-8 8 8" fill="none" stroke="#fff" stroke-width="3.5"/></svg></div>
</section>

<footer class="site-footer">
  <div class="brand">MIRAI</div>
  <ul class="flinks" style="left:140px"><li>HOME</li><li>ミライ・プロダクツとは</li><li>商品一覧</li><li>卸業者さまへ</li><li>WEBカタログ</li><li>会社案内</li></ul>
  <ul class="flinks" style="left:400px"><li>お問い合わせ</li><li>よくあるご質問</li><li>リンク</li><li>個人情報保護方針</li><li>サイトマップ</li></ul>
  <p class="search-h">SEARCH</p>
  <div class="search-box"><svg width="16" height="16" viewBox="0 0 16 16" fill="none" stroke="#9aa4ad" stroke-width="2"><circle cx="7" cy="7" r="5"/><path d="M11 11l4 4"/></svg>サイト内検索</div>
  <p class="company">ミライ・プロダクツ株式会社<small>〒000-0000<br>みどり県あおば市ひかり町1丁目2番3号</small></p>
  <p class="tel">TEL 0120-000-111<br>FAX 0120-000-222</p>
  <div class="copyright">© Copyright MIRAI PRODUCTS Co.,Ltd. All rights reserved.</div>
</footer>

</body>
</html>
```